Life Saving Rules KDBRX

Design a wallet/business card size document front and back to depict the attached lifesaving rules in the color scheme of the business logo attached. (Also attached is an example of a similar card)

Target Market(s)

End User - Field Employees

Industry/Entity Type

Refining

Requirements
Must have
• All Life Saving rules with graphics, using front and back of card, information needs to flow.
Nice to have
• Would like the design to be similar to the card uploaded but better with graphics

```html
<!DOCTYPE html>
<html lang="en">
<head>
<meta charset="utf-8">
<title>KDBRX Life Saving Rules – Wallet Card</title>
<link href="https://fonts.googleapis.com/css2?family=Rubik:wght@400;500;700&display=swap" rel="stylesheet">
<style>
  :root {
    --page-bg: #e4e4e4;
    --card-bg: #ffffff;
    --brand-blue: #0a6fc2;
    --sky-blue: #12a7e3;
    --brand-green: #3cbf3a;
    --ink: #1c1c1c;
  }
  * { box-sizing: border-box; margin: 0; padding: 0; }
  html, body { width: 726px; height: 1200px; overflow: hidden; }
  body {
    background: var(--page-bg);
    font-family: "Rubik", Arial, sans-serif;
    color: var(--ink);
    position: relative;
  }
  .card {
    position: absolute;
    left: 63px;
    width: 600px;
    height: 343px;
    background: var(--card-bg);
    box-shadow: 4px 6px 10px rgba(0,0,0,0.25);
  }
  .card--front { top: 227px; }
  .card--back { top: 630px; }

  .brand-name {
    position: absolute;
    font-weight: 700;
    color: var(--brand-blue);
    letter-spacing: 0.5px;
    text-align: center;
    white-space: nowrap;
  }
  .card--front .brand-name {
    left: 0; right: 0;
    top: 88px;
    font-size: 28px;
  }
  .card-title {
    position: absolute;
    left: 0; right: 0;
    top: 140px;
    text-align: center;
    font-size: 28px;
    font-weight: 700;
    color: var(--brand-green);
    letter-spacing: 0.3px;
  }
  .title-rule {
    position: absolute;
    left: 150px;
    width: 262px;
    top: 177px;
    height: 2px;
    background: var(--sky-blue);
  }

  .rule {
    position: absolute;
    width: 134px;
    text-align: center;
  }
  .rule-icon { display: block; margin: 0 auto; }
  .rule-text { font-weight: 400; }

  .card--front .rule { top: 203px; }
  .card--front .rule-icon { width: 60px; height: 60px; }
  .card--front .rule-icon--wide { width: 64px; height: 64px; margin-top: -2px; margin-bottom: -2px; }
  .card--front .rule-text { font-size: 12.5px; line-height: 14px; margin-top: 8px; }

  .card--back .rule-icon { width: 78px; height: 78px; }
  .card--back .rule-text { font-size: 13px; line-height: 14.6px; margin-top: 8px; }
  .card--back .row-1 { top: 17px; }
  .card--back .row-2 { top: 183px; }

  .back-brand {
    position: absolute;
    left: 446px;
    top: 268px;
    width: 140px;
    font-size: 18px;
  }

  .ln { fill: none; stroke-width: 2.2; stroke-linecap: round; stroke-linejoin: round; }
  .ln--thin { stroke-width: 1.4; }
  .blue { stroke: var(--sky-blue); }
  .green { stroke: var(--brand-green); }
</style>
</head>
<body>

<section class="card card--front" aria-label="Card front">
  <div class="brand-name">KDBRX</div>
  <h1 class="card-title">LIFE SAVING RULES</h1>
  <div class="title-rule"></div>

  <div class="rule" style="left:22px">
    <svg class="rule-icon" viewBox="0 0 60 60" role="img" aria-label="No smoking sign">
      <circle class="ln blue" cx="30" cy="30" r="27.5" stroke-width="3"/>
      <circle class="ln ln--thin green" cx="30" cy="30" r="23"/>
      <rect class="ln green" x="15" y="28" width="28" height="7" rx="1"/>
      <line class="ln green" x1="22" y1="28" x2="22" y2="35"/>
      <path class="ln green" d="M38 25c0-4 4-4 4-8M43 25c0-4 3-5 2-9"/>
      <line class="ln green" x1="14" y1="14" x2="46" y2="46"/>
    </svg>
    <p class="rule-text">Do not smoke outside of designated smoking areas</p>
  </div>
  <div class="rule" style="left:161px">
    <svg class="rule-icon" viewBox="0 0 60 60" role="img" aria-label="No alcohol or drugs sign">
      <circle class="ln blue" cx="30" cy="30" r="27.5" stroke-width="3"/>
      <circle class="ln ln--thin green" cx="30" cy="30" r="23"/>
      <path class="ln green" d="M28 13h5v7c3 2 4 4 4 7v18h-13V27c0-3 1-5 4-7z"/>
      <line class="ln green" x1="24" y1="33" x2="37" y2="33"/>
      <line class="ln green" x1="14" y1="46" x2="46" y2="14"/>
    </svg>
    <p class="rule-text">No alcohol or drugs while working or driving</p>
  </div>
  <div class="rule" style="left:300px">
    <svg class="rule-icon" viewBox="0 0 60 60" role="img" aria-label="No walking under loads sign">
      <circle class="ln blue" cx="30" cy="30" r="27.5" stroke-width="3"/>
      <circle class="ln ln--thin green" cx="30" cy="30" r="23"/>
      <path class="ln green" d="M30 12c5 0 7 4 7 9s-2 9-2 12h-10c0-4-2-7-2-12s3-9 7-9z"/>
      <path class="ln green" d="M25 38h10v4c0 3-2 5-5 5s-5-2-5-5z"/>
      <line class="ln green" x1="14" y1="46" x2="46" y2="14"/>
    </svg>
    <p class="rule-text" style="margin-top:10px">Do not walk under suspended loads</p>
  </div>
  <div class="rule" style="left:435px">
    <svg class="rule-icon rule-icon--wide" viewBox="0 0 64 64" role="img" aria-label="No phone while driving sign">
      <circle class="ln green" cx="32" cy="32" r="29.5" stroke-width="3"/>
      <circle class="ln ln--thin green" cx="32" cy="32" r="25"/>
      <rect class="ln green" x="22" y="13" width="20" height="38" rx="3"/>
      <line class="ln green" x1="22" y1="44" x2="42" y2="44"/>
      <line class="ln green" x1="29" y1="47.5" x2="35" y2="47.5"/>
      <line class="ln green" x1="48" y1="14" x2="16" y2="50"/>
    </svg>
    <p class="rule-text">While driving do not use your phone and do not exceed speed limits</p>
  </div>
</section>

<section class="card card--back" aria-label="Card back">
  <div class="rule row-1" style="left:14px">
    <svg class="rule-icon" viewBox="0 0 80 80" role="img" aria-label="Safety controls authorisation icon">
      <circle class="ln blue" cx="40" cy="40" r="37" stroke-width="3"/>
      <circle class="ln ln--thin blue" cx="40" cy="40" r="32"/>
      <rect class="ln green" x="22" y="19" width="36" height="44" rx="2"/>
      <path class="ln green" d="M33 19v-3h14v3"/>
      <circle class="ln ln--thin green" cx="40" cy="17" r="2"/>
      <path class="ln green" d="M27 36l4 5 7-9"/>
      <line class="ln green" x1="28" y1="55" x2="48" y2="30"/>
      <path class="ln green" d="M45 44a7 7 0 1 0 8 0M49 41v7"/>
    </svg>
    <p class="rule-text">Obtain authorisation before overriding or disabling safety controls</p>
  </div>
  <div class="rule row-1" style="left:161px">
    <svg class="rule-icon" viewBox="0 0 80 80" role="img" aria-label="Confined space entry icon">
      <circle class="ln green" cx="40" cy="10" r="6"/>
      <path class="ln green" d="M37 10l2 2 4-4"/>
      <rect class="ln blue" x="28" y="24" width="24" height="44" rx="2"/>
      <line class="ln blue" x1="33" y1="34" x2="47" y2="34"/>
      <line class="ln blue" x1="33" y1="44" x2="47" y2="44"/>
      <line class="ln blue" x1="33" y1="54" x2="47" y2="54"/>
      <line class="ln blue" x1="16" y1="70" x2="64" y2="70"/>
      <path class="ln green" d="M6 70h5M69 70h5"/>
      <line class="ln green" x1="34" y1="75" x2="46" y2="75"/>
    </svg>
    <p class="rule-text">Obtain authorisation before entering a confined space</p>
  </div>
  <div class="rule row-1" style="left:308px">
    <svg class="rule-icon" viewBox="0 0 80 80" role="img" aria-label="Energy isolation icon">
      <path class="ln blue" d="M34 8h10v5h6v56H28V13h6z"/>
      <path class="ln green" d="M42 24l-9 14h8l-6 14"/>
      <circle class="ln blue" cx="53" cy="62" r="11" fill="#fff"/>
      <line class="ln blue" x1="48" y1="62" x2="58" y2="62" stroke-width="3"/>
    </svg>
    <p class="rule-text">Verify isolation and zero energy before work begins</p>
  </div>
  <div class="rule row-1" style="left:451px">
    <svg class="rule-icon" viewBox="0 0 80 80" role="img" aria-label="Flammables and ignition icon">
      <path class="ln blue" d="M26 70c-9-6-10-18-4-27 2 5 5 6 7 6-2-10 3-20 13-27-1 8 2 12 6 14 2-4 2-7 1-10 8 6 12 17 10 28-1 7-5 12-9 16"/>
      <path class="ln green" d="M14 18c-3 4 3 7 0 11M24 12c-3 4 3 7 0 11M60 14c-3 4 3 7 0 11M68 20c-3 4 3 7 0 11"/>
    </svg>
    <p class="rule-text">Control flammables and ignition sources</p>
  </div>

  <div class="rule row-2" style="left:14px">
    <svg class="rule-icon" viewBox="0 0 80 80" role="img" aria-label="Lifting operations icon">
      <circle class="ln blue" cx="40" cy="40" r="37" stroke-width="3"/>
      <line class="ln green" x1="26" y1="24" x2="26" y2="64"/>
      <line class="ln green" x1="31" y1="24" x2="31" y2="64"/>
      <rect class="ln green" x="22" y="17" width="13" height="8"/>
      <line class="ln green" x1="35" y1="21" x2="58" y2="21"/>
      <line class="ln green" x1="54" y1="21" x2="54" y2="30"/>
      <path class="ln green" d="M47 36l8-6 6 8-8 6z"/>
      <rect class="ln green" x="38" y="50" width="22" height="12"/>
      <line class="ln green" x1="46" y1="56" x2="55" y2="56"/>
    </svg>
    <p class="rule-text">Plan lifting operations and control the area</p>
  </div>
  <div class="rule row-2" style="left:161px">
    <svg class="rule-icon" viewBox="0 0 80 80" role="img" aria-label="Work permit checklist icon">
      <circle class="ln blue" cx="40" cy="40" r="37" stroke-width="3"/>
      <rect class="ln green" x="24" y="17" width="32" height="46" rx="2"/>
      <path class="ln green" d="M30 14v6M36 14v6M44 14v6M50 14v6"/>
      <path class="ln green" d="M29 30l2 2 3-4M29 40l2 2 3-4M29 50l2 2 3-4"/>
      <rect class="ln green" x="38" y="28" width="13" height="4" rx="2"/>
      <rect class="ln green" x="38" y="38" width="13" height="4" rx="2"/>
      <rect class="ln green" x="38" y="48" width="13" height="4" rx="2"/>
    </svg>
    <p class="rule-text">Work with a valid permit when required</p>
  </div>
  <div class="rule row-2" style="left:308px">
    <svg class="rule-icon" viewBox="0 0 80 80" role="img" aria-label="Working at height protection icon">
      <circle class="ln blue" cx="40" cy="40" r="37" stroke-width="3"/>
      <path class="ln green" d="M40 16l14 5v10c0 9-6 14-14 17-8-3-14-8-14-17V21z"/>
      <path class="ln green" d="M40 23v16M34 34l6 6 6-6"/>
      <path class="ln green" d="M20 56h10l6 4h12c2 0 2 3 0 3H38M20 62h14l18 0 8-8"/>
    </svg>
    <p class="rule-text">Protect yourself against a fall when working at height</p>
  </div>

  <div class="brand-name back-brand">KDBRX</div>
</section>

</body>
</html>
```